Professional business cards for real estate development company

I need business cards for my new real estate development company. The company, "KORVA" is a real estate development, investment, and advisory firm with a focus on multifamily, office, and mixed-use projects across primary and secondary markets in the Southeast United States.

Style preference is modern

Industry/Entity Type

Real Estate Development

Contact Information for Business Card

The business cards need to include:
Name
Title
Mailing Address
Phone Number
Web Address

Logo is attached. I would like white to be the primary color with incorporation of the company colors: #232D3A and #B5A451

Font styles to use
Other font styles liked:
• Montserrat, Avenir

Requirements
Must have
• Company Logo. No need to include the company name since the name is in the logo.
Should not have
• No line type designs

```html
<!DOCTYPE html>
<html lang="en">
<head>
<meta charset="utf-8">
<title>KORVA Business Cards</title>
<link href="https://fonts.googleapis.com/css2?family=Montserrat:wght@600;700&display=swap" rel="stylesheet">
<style>
  :root {
    --stage: #000000;
    --card: #ffffff;
    --gold: #b5a451;
    --gold-deep: #857a44;
    --gold-mid: #9c8f4c;
    --navy: #232d3a;
  }
  html, body {
    margin: 0;
    width: 1200px;
    height: 1200px;
    overflow: hidden;
    background: var(--stage);
  }
  .stage {
    position: relative;
    width: 1200px;
    height: 1200px;
  }
  .card {
    position: absolute;
    left: 326px;
    width: 548px;
    height: 306px;
  }
  .card--front { top: 254px; }
  .card--back { top: 639px; }
  .card svg { display: block; width: 100%; height: 100%; }
  .brand-name {
    font-family: "Montserrat", sans-serif;
    font-weight: 600;
    letter-spacing: 4px;
  }
  .contact-text {
    font-family: "Montserrat", sans-serif;
    font-weight: 700;
    fill: var(--navy);
  }
</style>
</head>
<body>
<main class="stage">

  <div class="card card--front">
    <svg viewBox="0 0 756 422" aria-label="Card front">
      <defs>
        <clipPath id="front-shape"><rect width="756" height="422" rx="60"/></clipPath>
        <linearGradient id="front-gold" x1="0" y1="0" x2="1" y2="0.4">
          <stop offset="0" stop-color="var(--gold-deep)"/>
          <stop offset="0.55" stop-color="var(--gold)"/>
          <stop offset="1" stop-color="var(--gold-mid)"/>
        </linearGradient>
      </defs>
      <g clip-path="url(#front-shape)">
        <rect class="card-base" width="756" height="422" fill="var(--card)"/>
        <path class="decor-area" role="img" aria-label="Decorative gold wave artwork"
              d="M0,290 C220,350 480,300 756,240 L756,422 L0,422 Z" fill="url(#front-gold)"/>
        <text class="brand-name" x="378" y="200" text-anchor="middle" font-size="72" fill="var(--gold)">KORVA</text>
      </g>
    </svg>
  </div>

  <div class="card card--back">
    <svg viewBox="0 0 756 422" aria-label="Card back with contact details">
      <defs>
        <clipPath id="back-shape"><rect width="756" height="422" rx="60"/></clipPath>
        <linearGradient id="back-gold" x1="0" y1="1" x2="1" y2="0">
          <stop offset="0" stop-color="var(--gold-deep)"/>
          <stop offset="0.6" stop-color="var(--gold)"/>
          <stop offset="1" stop-color="var(--gold-mid)"/>
        </linearGradient>
      </defs>
      <g clip-path="url(#back-shape)">
        <rect class="card-base" width="756" height="422" fill="var(--card)"/>
        <path class="decor-area" role="img" aria-label="Decorative gold wave artwork"
              d="M425,0 C475,100 460,240 400,320 C370,360 340,395 310,422 L756,422 L756,0 Z" fill="url(#back-gold)"/>
        <text class="brand-name" x="597" y="268" text-anchor="middle" font-size="56" fill="var(--card)">KORVA</text>

        <text class="contact-text" x="366" y="118" text-anchor="end" font-size="16">(555) 123-4567</text>
        <text class="contact-text" x="366" y="138" text-anchor="end" font-size="16">(555) 123-4567</text>
        <g class="icon icon--phone" transform="translate(397,121)">
          <circle r="22" fill="var(--navy)"/>
          <path d="M-9,-10 L-4,-12 L0,-4 L-3,-1 C-1,3 2,6 5,8 L8,5 L15,9 L13,14 C3,15 -11,1 -9,-10 Z" fill="var(--card)"/>
        </g>

        <text class="contact-text" x="345" y="190" text-anchor="end" font-size="21">www.companyname.com</text>
        <g class="icon icon--web" transform="translate(383,187)" fill="none" stroke="var(--card)" stroke-width="2">
          <circle r="22" fill="var(--navy)" stroke="none"/>
          <circle r="13"/>
          <ellipse rx="6" ry="13"/>
          <line x1="-13" y1="0" x2="13" y2="0"/>
          <line x1="-11" y1="-6" x2="11" y2="-6"/>
          <line x1="-11" y1="6" x2="11" y2="6"/>
        </g>

        <text class="contact-text" x="314" y="249" text-anchor="end" font-size="21">company@name.com</text>
        <g class="icon icon--mail" transform="translate(349,245)" fill="none" stroke="var(--card)" stroke-width="2">
          <circle r="22" fill="var(--navy)" stroke="none"/>
          <rect x="-13" y="-9" width="26" height="18"/>
          <polyline points="-13,-9 0,2 13,-9"/>
          <line x1="-13" y1="9" x2="-3" y2="0"/>
          <line x1="13" y1="9" x2="3" y2="0"/>
        </g>

        <text class="contact-text" x="47" y="299" font-size="20">First Address line</text>
        <text class="contact-text" x="47" y="319" font-size="20">Second Address line</text>
        <g class="icon icon--home" transform="translate(292,301)">
          <circle r="22" fill="var(--navy)"/>
          <path d="M0,-13 L-14,0 L-10,0 L-10,12 L-3,12 L-3,4 L3,4 L3,12 L10,12 L10,0 L14,0 Z" fill="var(--card)"/>
        </g>
      </g>
    </svg>
  </div>

</main>
</body>
</html>
```